Bruntel general construction

We need an website that are similar to these websites:
https://www.morvexa.com/en/
https://dulnari.com/company/

but with a tweak. Do not copy the entire website but atleast similar and yet better than them.

For reference this our current website.
https://bruntel.ph/

For the winning Designer please help us with the migration from our old website to the new redesign website.

```html
<!DOCTYPE html>
<html lang="en">
<head>
<meta charset="utf-8">
<title>Bruntel — Sustainability Starts Here</title>
<link href="https://fonts.googleapis.com/css2?family=Raleway:wght@600;700;800&family=Roboto:wght@400;500;700&display=swap" rel="stylesheet">
<style>
:root{
  --orange:#f15a24;
  --amber:#fbb615;
  --blue:#0a8fd6;
  --navy:#0b1126;
  --ink:#111;
  --text:#444;
  --grey:#f2f2f2;
  --white:#fff;
}
*{box-sizing:border-box;margin:0;padding:0}
html,body{width:1200px;height:3687px;overflow:hidden;background:var(--white)}
body{position:relative;font-family:'Roboto',sans-serif;color:var(--text)}
.abs{position:absolute}
.btn{position:absolute;display:flex;align-items:center;justify-content:center;border-radius:30px;font:700 14px 'Roboto',sans-serif;text-transform:uppercase;color:#fff;background:linear-gradient(90deg,var(--orange),var(--amber));box-shadow:0 0 0 4px #fff,0 0 0 5px #e8e8e8}
.btn.outline{background:#fff;color:var(--blue);box-shadow:0 0 0 1px #cfd8df}
.btn.blue{background:var(--blue);box-shadow:0 0 0 4px #fff,0 0 0 5px #cde4f2}
h2.section-title{position:absolute;left:0;width:1200px;text-align:center;font:700 40px 'Raleway',sans-serif;color:var(--ink)}
.underline{position:absolute;height:3px;background:linear-gradient(90deg,var(--orange),var(--amber))}

.header{position:absolute;top:0;left:0;width:1200px;height:145px;background:#fff;z-index:3}
.logo-disc{position:absolute;left:115px;top:-5px;width:200px;height:205px;border-radius:0 0 100px 100px;background:#fff;z-index:4}
.logo-name{position:absolute;left:0;width:200px;top:135px;text-align:center;font:700 22px 'Roboto',sans-serif;color:var(--blue);letter-spacing:1px}
.logo-dot{position:absolute;left:78px;top:40px;width:44px;height:44px;border-radius:50%;background:linear-gradient(180deg,var(--amber),var(--orange))}
.nav{position:absolute;top:105px;right:111px;display:flex;gap:35px;font:700 14px 'Roboto',sans-serif;color:var(--ink)}
.nav .active{color:var(--blue);border-bottom:2px solid var(--blue);padding-bottom:2px}
.call{position:absolute;left:830px;top:22px;width:62px;height:62px;border-radius:50%;background:#fff;box-shadow:0 2px 10px rgba(0,0,0,.15)}
.call-label{position:absolute;left:906px;top:30px;font:500 12px 'Roboto',sans-serif;color:#888}
.call-num{position:absolute;left:906px;top:49px;font:500 20px 'Roboto',sans-serif;color:var(--blue)}
.divider-v{position:absolute;left:806px;top:24px;width:1px;height:58px;background:#ddd}

.hero{position:absolute;top:145px;left:0;width:1200px;height:660px;background:linear-gradient(180deg,#3d5d86 0%,#7a8aa3 30%,#c48a4c 62%,#5a3a22 100%)}
.hero-title{position:absolute;top:358px;left:0;width:1200px;text-align:center;font:800 45px 'Raleway',sans-serif;color:#fff}
.hero-sub{position:absolute;top:423px;left:290px;width:620px;text-align:center;font:500 22px/29px 'Roboto',sans-serif;color:#fff}
.counter{position:absolute;left:1134px;top:462px;transform:rotate(-90deg);transform-origin:left top;font:500 15px 'Roboto',sans-serif;color:#fff;letter-spacing:2px;white-space:nowrap}
.counter b{color:var(--amber);font-weight:500}
.dots{position:absolute;top:741px;left:566px;display:flex;gap:12px}
.dots i{width:13px;height:13px;border:2px solid #fff;border-radius:50%}
.dots i.on{background:#fff}

.who-deco{position:absolute;left:112px;top:1178px;width:178px;height:178px;border-radius:50%;background:#eaf4fb}
.who-photo{position:absolute;left:145px;top:886px;width:434px;height:434px;border-radius:50%;background:linear-gradient(180deg,#8fbde6 0%,#cde1ef 38%,#5b8a3c 55%,#3f6a85 80%,#2c3d5c 100%);border:3px solid var(--amber);border-left-color:var(--orange)}
.who-title{position:absolute;left:653px;top:896px;font:700 37px 'Raleway',sans-serif;color:var(--ink)}
.who-text{position:absolute;left:653px;top:972px;width:436px;font:400 14.5px/25px 'Roboto',sans-serif;text-align:justify;color:var(--text)}
.who-text p+p{margin-top:12px}

.services-bg{position:absolute;top:1434px;left:0;width:1200px;height:1094px;background:var(--grey)}
.card{position:absolute;width:303px;height:470px;background:#fff;border-radius:14px;box-shadow:0 4px 18px rgba(0,0,0,.12);z-index:2}
.card .ph{position:absolute;left:8px;top:8px;width:287px;height:210px;border-radius:10px}
.card .icon{position:absolute;left:110px;top:178px;width:84px;height:84px;border-radius:50%;background:var(--blue);border:6px solid #fff;display:flex;align-items:center;justify-content:center}
.card h3{position:absolute;top:290px;left:0;width:100%;text-align:center;font:700 17px 'Roboto',sans-serif;color:var(--ink)}
.card p{position:absolute;top:320px;left:25px;width:253px;height:76px;overflow:hidden;text-align:center;font:400 14.5px/25px 'Roboto',sans-serif;color:var(--text)}
.card .btn{left:78px;top:402px;width:146px;height:44px}
.arrow{position:absolute;top:1733px}
.tagline{position:absolute;top:2198px;left:100px;width:1000px;text-align:center;font:800 38px/50px 'Raleway',sans-serif;color:#fff}

.news-photo{position:absolute;border-radius:16px}
.news-date{position:absolute;height:32px;padding:0 16px;border-radius:16px;background:var(--blue);color:#fff;font:700 12px/32px 'Roboto',sans-serif}
.news-h{position:absolute;font:500 17.5px/26px 'Roboto',sans-serif;color:var(--ink);text-transform:uppercase}
.read{position:absolute;font:500 14px 'Roboto',sans-serif;color:var(--orange);border-bottom:1px solid var(--orange)}
.feature-box{position:absolute;left:150px;top:2969px;width:404px;height:176px;background:#fff;border-radius:14px;box-shadow:0 4px 18px rgba(0,0,0,.1)}

.footer{position:absolute;left:0;top:3260px;width:1200px;height:427px}
.f-logo{position:absolute;left:111px;top:3433px;width:164px;height:164px;border-radius:50%;background:#fff}
.f-col h4{position:absolute;font:700 14px 'Roboto',sans-serif;color:#fff;border-bottom:1px solid #fff;padding-bottom:3px}
.f-links{position:absolute;left:323px;top:3459px;font:400 13px/26.5px 'Roboto',sans-serif;color:#fff;list-style:none}
.f-item{position:absolute;left:481px;display:flex;align-items:flex-start;gap:16px;font:400 13.5px/21px 'Roboto',sans-serif;color:#fff}
.f-item .ic{width:26px;height:26px;border-radius:50%;background:#1f2740;display:flex;align-items:center;justify-content:center;flex:none}
.email-field{position:absolute;left:804px;top:3459px;width:283px;height:46px;border-radius:23px;background:#fff;font:400 14px/46px 'Roboto',sans-serif;color:#666;padding-left:18px}
.f-rule{position:absolute;left:111px;top:3625px;width:978px;height:1px;background:#252d45}
.copyright{position:absolute;left:0;width:1200px;top:3645px;text-align:center;font:400 12.5px 'Roboto',sans-serif;color:#fff}
.social{position:absolute;top:3635px;width:36px;height:36px;border-radius:50%}
</style>
</head>
<body>

<header class="header">
  <div class="divider-v"></div>
  <div class="btn" style="left:622px;top:30px;width:156px;height:46px">Get a Quote</div>
  <div class="call">
    <svg width="62" height="62" viewBox="0 0 62 62"><circle cx="31" cy="31" r="17" fill="none" stroke="#f37a22" stroke-width="3"/><path d="M24 25c1-2 3-2 4 0l1 3-2 2c1 2 3 4 5 5l2-2 3 1c2 1 2 3 0 4-4 3-15-8-13-13z" fill="#f37a22"/></svg>
  </div>
  <div class="call-label">CALL US:</div>
  <div class="call-num">+63 (0) 46 555-0182</div>
  <nav class="nav">
    <span class="active">HOME</span><span>ABOUT US</span><span>OUR SERVICES</span><span>OUR TEAM</span><span>NEWS &amp; MEDIA</span><span>CONTACT US</span>
  </nav>
</header>
<div class="logo-disc"><div class="logo-dot"></div><div class="logo-name">BRUNTEL</div></div>

<section class="hero" role="img" aria-label="Industrial refinery plant at dusk under a cloudy sky"></section>
<svg class="abs" style="left:0;top:600px" width="1200" height="240" viewBox="0 0 1200 240">
  <path d="M0 34 Q600 334 1200 34 L1200 240 L0 240Z" fill="#fff"/>
  <path d="M0 30 Q600 330 1200 30" fill="none" stroke="#0a8fd6" stroke-width="14"/>
  <path d="M0 19 Q600 319 1200 19" fill="none" stroke="#fff" stroke-width="6"/>
</svg>
<h1 class="hero-title">SUSTAINABILITY STARTS HERE.</h1>
<p class="hero-sub">We assist in the advancement of an environmental friendly society by providing our services to world-renowned environmental EPC companies.</p>
<div class="btn" style="left:520px;top:538px;width:158px;height:48px">Get Started</div>
<div class="counter"><b>02</b> / 03</div>
<svg class="abs" style="left:1136px;top:355px" width="14" height="140" viewBox="0 0 14 140"><path d="M3 8l4-4 4 4M3 132l4 4 4-4" fill="none" stroke="#fff" stroke-width="1.5"/></svg>
<div class="dots"><i></i><i class="on"></i><i></i></div>

<div class="who-deco"></div>
<div class="who-photo" role="img" aria-label="Wind turbines, a hydro dam and solar panel fields in green hills"></div>
<h2 class="who-title">WHO WE ARE</h2>
<div class="underline" style="left:653px;top:943px;width:88px"></div>
<div class="who-text">
  <p>With more than four years of established business relationships with various blue chip clients and major construction companies, we at Bruntel can provide a wide range of services to the oil, gas, energy, and environmental sectors. While we aim for sustainability and profitability in all our projects, we strive to protect the environment and the health and safety of our people and the communities where we operate.</p>
  <p>We deliver what we promise and in doing so exceed our client's expectations. We are able to achieve this by providing a host of services to different industries from one source, reducing our client's overheads in the process.</p>
</div>
<div class="btn" style="left:656px;top:1285px;width:156px;height:46px">Get Started</div>

<div class="services-bg"></div>
<svg class="abs" style="left:0;top:1880px" width="1200" height="648" viewBox="0 0 1200 648">
  <defs><linearGradient id="band" x1="0" x2="1"><stop offset="0" stop-color="#f15a24"/><stop offset="1" stop-color="#fbb615"/></linearGradient></defs>
  <path d="M0 30 C250 0 500 40 700 60 C900 80 1100 60 1200 130 L1200 648 L0 648Z" fill="url(#band)"/>
</svg>
<h2 class="section-title" style="top:1522px">OUR SERVICES</h2>
<div class="underline" style="left:557px;top:1572px;width:86px"></div>

<svg class="arrow" style="left:36px" width="42" height="28" viewBox="0 0 42 28"><path d="M40 14H3M14 3L3 14l11 11" fill="none" stroke="#666" stroke-width="2.5"/></svg>
<svg class="arrow" style="left:1122px" width="42" height="28" viewBox="0 0 42 28"><path d="M2 14h37M28 3l11 11-11 11" fill="none" stroke="#666" stroke-width="2.5"/></svg>

<div class="card" style="left:112px;top:1609px">
  <div class="ph" role="img" aria-label="Aerial view of circular water treatment tanks among trees" style="background:linear-gradient(135deg,#3f7a3a,#2f8fa0 50%,#2e6b44)"></div>
  <div class="icon"><svg width="40" height="40" viewBox="0 0 40 40"><circle cx="20" cy="20" r="15" fill="none" stroke="#fff" stroke-width="2"/><path d="M20 11c4 6 6 9 6 12a6 6 0 0 1-12 0c0-3 2-6 6-12z" fill="none" stroke="#fff" stroke-width="2"/></svg></div>
  <h3>WATER TREATMENT</h3>
  <p>We have in-house expertise for the onstruction of Sewage Water Treatment Plants (SWTP) and utility systems for industrial clients.</p>
  <div class="btn outline">Learn More</div>
</div>
<div class="card" style="left:448px;top:1635px">
  <div class="ph" role="img" aria-label="Engineers in hard hats reviewing plans on a construction site" style="background:linear-gradient(135deg,#9fb6cc,#c9d4de 45%,#50627a)"></div>
  <div class="icon" style="background:linear-gradient(180deg,var(--orange),var(--amber))"><svg width="40" height="40" viewBox="0 0 40 40"><path d="M8 32h24M12 32V16h8v16M20 20h8v12M12 10h18M26 10v6" fill="none" stroke="#fff" stroke-width="2"/></svg></div>
  <h3>CONSTRUCTION</h3>
  <p>Our experience of working to international standards and complying with international business ethics and safety codes.</p>
  <div class="btn">Learn More</div>
</div>
<div class="card" style="left:785px;top:1609px">
  <div class="ph" role="img" aria-label="Oil pump jack silhouetted against a golden sunset" style="background:linear-gradient(180deg,#f3b45a,#c8722c 60%,#5a2e12)"></div>
  <div class="icon"><svg width="40" height="40" viewBox="0 0 40 40"><path d="M8 30h24l-3 4H11zM12 30V20h16v10M16 20V8h4v12M22 14h6" fill="none" stroke="#fff" stroke-width="2"/></svg></div>
  <h3>OIL AND GAS</h3>
  <p>We are known in the oil and gas industry for our ability to provide multi skilled, reliable, and cost-effective teams.</p>
  <div class="btn outline">Learn More</div>
</div>

<h2 class="tagline">OUTSTANDING SAFETY, ENVIRONMENTAL AWARENESS, AND WORLD-CLASS QUALITY DEFINES THE WAY WE WORK.</h2>
<div class="abs" style="left:557px;top:2356px;width:86px;height:3px;background:#fff"></div>
<div class="btn blue" style="left:521px;top:2397px;width:158px;height:46px">Contact Us</div>

<h2 class="section-title" style="top:2646px">LATEST NEWS</h2>
<div class="underline" style="left:557px;top:2694px;width:86px"></div>

<div class="news-photo" role="img" aria-label="Aerial view of a large industrial power facility" style="left:107px;top:2736px;width:446px;height:282px;background:linear-gradient(180deg,#b9c4cc,#8f9da6 55%,#5d6a60)"></div>
<div class="feature-box"></div>
<div class="news-date" style="left:178px;top:2952px">&#9638; 05 FEB 2026</div>
<div class="news-h" style="left:176px;top:3002px;width:360px">Environmental Protection Ndustry a Job Creator</div>
<p class="abs" style="left:176px;top:3059px;width:350px;font:400 14.5px/22px 'Roboto',sans-serif;color:#444">Sed ut perspiciatis unde omnis iste natus error sit voluptatem accusantium...</p>
<div class="read" style="left:176px;top:3104px">READ MORE</div>

<div class="news-photo" role="img" aria-label="Gas processing columns lit at dusk" style="left:568px;top:2736px;width:250px;height:193px;background:linear-gradient(180deg,#2a3563,#5a6a94 60%,#c9c9d0)"></div>
<div class="news-date" style="left:842px;top:2756px">&#9638; 05 FEB 2026</div>
<div class="news-h" style="left:842px;top:2806px;width:250px">Heatline Group to Supply Turbocharger Technology...</div>
<div class="read" style="left:842px;top:2896px">READ MORE</div>

<div class="news-photo" role="img" aria-label="Workers in safety vests reviewing a tablet at a port" style="left:568px;top:2950px;width:250px;height:193px;background:linear-gradient(135deg,#6fa4d4,#e2a94a 55%,#c9d64a)"></div>
<div class="news-date" style="left:842px;top:2970px">&#9638; 05 FEB 2026</div>
<div class="news-h" style="left:842px;top:3020px;width:260px">Positive Signs for Oilfield Services Sector as U.S. Onshore Market...</div>
<div class="read" style="left:842px;top:3110px">READ MORE</div>

<svg class="footer" viewBox="0 0 1200 427">
  <path d="M0 185 Q600 -120 1200 185 L1200 427 L0 427Z" fill="#0b1126"/>
  <path d="M0 185 Q600 -120 1200 185" fill="none" stroke="#0a8fd6" stroke-width="12"/>
  <path d="M0 168 Q600 -137 1200 168" fill="none" stroke="#fff" stroke-width="6"/>
</svg>
<div class="f-logo">
  <div class="abs" style="left:60px;top:26px;width:44px;height:44px;border-radius:50%;background:linear-gradient(180deg,var(--amber),var(--orange))"></div>
  <div class="abs" style="left:0;top:96px;width:164px;text-align:center;font:700 18px 'Roboto',sans-serif;color:var(--blue)">BRUNTEL</div>
</div>
<div class="f-col"><h4 style="left:323px;top:3415px">QUICK LINKS</h4></div>
<ul class="f-links"><li>Home</li><li>About Us</li><li>Our Services</li><li>Our Team</li><li>News &amp; Media</li><li>Contact Us</li></ul>
<div class="f-col"><h4 style="left:481px;top:3415px">CONTACT INFO</h4></div>
<div class="f-item" style="top:3459px"><span class="ic"><svg width="12" height="12" viewBox="0 0 12 12"><path d="M2 1l2 0 1 3-1 1c1 2 2 3 4 4l1-1 3 1v2c-6 1-11-4-10-10z" fill="#f8a51b"/></svg></span>+63 (0) 46 555-0182</div>
<div class="f-item" style="top:3504px"><span class="ic"><svg width="12" height="10" viewBox="0 0 12 10"><rect x="0" y="0" width="12" height="10" fill="#f8a51b"/><path d="M0 0l6 5 6-5" fill="none" stroke="#1f2740"/></svg></span>info@bruntel.ph</div>
<div class="f-item" style="top:3549px"><span class="ic"><svg width="10" height="13" viewBox="0 0 10 13"><path d="M5 13C1 8 0 6 0 5a5 5 0 0 1 10 0c0 1-1 3-5 8z" fill="#f8a51b"/></svg></span>18 Verano Lane Brgy. Maliwan<br>Talbora City, Lenoria Philippines 4127</div>
<div class="f-col"><h4 style="left:804px;top:3415px">NEWSLETTER</h4></div>
<div class="email-field">Email Address
  <svg class="abs" style="right:18px;top:15px" width="18" height="16" viewBox="0 0 18 16"><path d="M0 8L18 0 14 16 9 11 16 3 7 10z" fill="#f8a51b"/></svg>
</div>
<div class="f-rule"></div>
<div class="copyright">© 2026 &nbsp; / &nbsp; All Rights Reserved</div>
<div class="social" aria-label="Social link" style="left:1007px;background:#fff"></div>
<div class="social" aria-label="Social link" style="left:1050px;background:linear-gradient(180deg,var(--orange),var(--amber))"></div>

</body>
</html>
```